KRV Business Cards

We are a local commercial development company based in Silicon Valley and we would like a new business card. I've attached a copy of our company brochure to give a flavor of what we do, our logo, info company colors/graphics, and our current business card. We don't necessarily need a crazy makeover, but would like something that feels a little bit more "fresh" and modern (we've had the same business card design for 15+ years), but still in keeping with our overall brand -- clean, high-quality, modern but timeless. Would like to add our website to the info on the card (www.velmara.com) and would like the flexibility for some folks to have an efax number listed and some not to have that included (without it looking like there is a hole).

```html
<!DOCTYPE html>
<html lang="en">
<head>
<meta charset="utf-8">
<title>KRV Business Cards</title>
<link href="https://fonts.googleapis.com/css2?family=Work+Sans:wght@400;600;700&display=swap" rel="stylesheet">
<style>
  :root {
    --backdrop: #242424;
    --card-white: #ffffff;
    --brand-navy: #2c4a66;
    --brand-slate: #36566f;
    --brand-slate-light: #4a6379;
    --ink: #3a3a3a;
    --on-dark: #ffffff;
  }
  * { margin: 0; padding: 0; box-sizing: border-box; }
  html, body {
    width: 1200px;
    height: 800px;
    overflow: hidden;
    background: var(--backdrop);
    font-family: "Work Sans", Arial, sans-serif;
  }
  .canvas { position: relative; width: 1200px; height: 800px; }

  .card {
    position: absolute;
    left: 347px;
    width: 499px;
    height: 284px;
  }
  .card-front { top: 110px; background: var(--card-white); }
  .card-back {
    top: 417px;
    background: radial-gradient(circle at 92% 18%, var(--brand-slate-light) 0%, var(--brand-slate) 45%);
  }

  .holder-name {
    position: absolute;
    left: 43px; top: 45px;
    font-size: 18px;
    font-weight: 600;
    letter-spacing: 1.6px;
    color: var(--brand-navy);
  }
  .holder-title {
    position: absolute;
    left: 43px; top: 68px;
    font-size: 13.5px;
    color: var(--ink);
  }
  .accent-rule {
    position: absolute;
    left: 42px; top: 110px;
    width: 28px; height: 2px;
    background: var(--brand-navy);
  }
  .contact-list {
    position: absolute;
    left: 43px; top: 147px;
    list-style: none;
    font-size: 11.5px;
    line-height: 15px;
    color: var(--ink);
  }
  .contact-label { font-weight: 600; color: var(--brand-navy); }
  .front-web {
    position: absolute;
    left: 43px; top: 233px;
    font-size: 11.5px;
    color: var(--brand-navy);
  }
  .front-web strong { font-weight: 600; }
  .company-name-front {
    position: absolute;
    left: 306px; top: 186px;
    font-size: 18px;
    line-height: 21px;
    letter-spacing: 0.5px;
    color: var(--brand-navy);
    text-transform: uppercase;
  }

  .company-name-back {
    position: absolute;
    left: 29px; top: 100px;
    font-size: 34px;
    line-height: 38px;
    letter-spacing: 0.5px;
    color: var(--on-dark);
    text-transform: uppercase;
  }
  .back-web {
    position: absolute;
    left: 34px; top: 236px;
    font-size: 15px;
    font-weight: 600;
    color: var(--on-dark);
  }
</style>
</head>
<body>
<main class="canvas">
  <section class="card card-front">
    <h1 class="holder-name">NORA J. HALDEN</h1>
    <p class="holder-title">Partner</p>
    <div class="accent-rule"></div>
    <ul class="contact-list">
      <li><span class="contact-label">Phone:</span> (08) 5550 1427</li>
      <li><span class="contact-label">Email:</span> mobile@velmara.com</li>
      <li><span class="contact-label">Address:</span> 88 Orchard Lane</li>
      <li>Mountain Grove, California 94010</li>
    </ul>
    <p class="front-web">www.<strong>velmara</strong>.com</p>
    <p class="company-name-front">KRV<br>Development<br>Company, LLC</p>
  </section>

  <section class="card card-back">
    <p class="company-name-back">KRV<br>Development<br>Company, LLC</p>
    <p class="back-web">www.velmara.com</p>
  </section>
</main>
</body>
</html>
```